WordPress Website Design - Brennick Auction

Need a WordPress design for an auction company wanting a responsive, simple and easy to use site. Current site to be upgraded: http://www.brennickauctions.example/

A site the client mentions liking is http://www.taverlyauction.example. The attached logo color can be changed to suit your design - a different red, or green perhaps.

Industry/Entity Type

It Company

Number of Pages Required

1 page

Font styles to use
Serif
Sans Serif

Requirements
Must have
• Keep in mind this site will be built on a responsive theme.
• Site navigation: 1) Home, 2) Auctions, 3) Real Estate Listings, 4) Services, 5) Appraisals, 6) The Gavel Hall, 7) About Us, 8) Contact Us
• Site will have large, prominent full width (960px) slideshow - please pick one of the 3 attached images. Colors can be different than current site - wants a brighter site, colors complementing the logo. Home page will have auction list (the look of the auction list can be seen at http://www.northgateholdingsweb.example/auction-calendar/)
• The widgets in the sidebar/header are: Email signup form, social media(FB Chirpline, ClipStream), News & Events blog, Testimonials, Featured Auctions, Featured Listings widget.
• Footer will have smaller company logo(below), contact info, and attached association logos.
• Gordon Brennick Auction-Realty
• 3817 Pelham Court • Castor Falls, IN 47088
• dominic@brennickauctions.example
• 812.555.0146
• 877.555.0193
Nice to have
• Design of dropdown menus: under Auctions, 1) Current Auctions, 2) Online Auctions, 3) Past Auctions

```html
<!DOCTYPE html>
<html lang="en">
<head>
<meta charset="utf-8">
<title>Brennick Auction — Personal · Auctions · Solutions</title>
<link href="https://fonts.googleapis.com/css2?family=Open+Sans:wght@400;600;700;800&display=swap" rel="stylesheet">
<style>
:root{
  --red:#d6222f;
  --red-dark:#b51924;
  --ink:#333333;
  --muted:#777777;
  --line:#dddddd;
  --panel:#f1f1f1;
  --widget-head:#3a3a3a;
  --page:#ffffff;
  --footer:#ececec;
  --footer-base:#dcdcdc;
}
*{box-sizing:border-box;margin:0;padding:0}
html,body{width:1200px;height:3100px;overflow:hidden}
body{background:var(--page);font-family:"Open Sans",Arial,sans-serif;color:var(--ink);font-size:13px;line-height:1.5}
a{color:inherit;text-decoration:none}

/* header */
.site-header{height:60px;display:flex;align-items:center;justify-content:space-between;padding:0 100px;background:#fff}
.brand{display:flex;align-items:center;gap:8px;font-size:22px;font-weight:700;color:var(--red);letter-spacing:-.3px}
.brand-mark{width:10px;height:10px;background:var(--red)}
.main-nav{display:flex;gap:30px;font-size:12px;color:#555}
.main-nav a.active{color:var(--red)}

/* hero */
.hero{position:relative;height:310px;background:linear-gradient(180deg,#8d9aa5 0%,#6f7b70 45%,#4f5f3e 75%,#3d4a31 100%);display:flex;flex-direction:column;align-items:center;justify-content:center;color:#fff}
.hero::after{content:"";position:absolute;inset:0;background:rgba(0,0,0,.18)}
.hero > *{position:relative;z-index:1}
.hero-title{font-size:40px;font-weight:800;letter-spacing:5px;text-transform:uppercase;text-shadow:0 2px 6px rgba(0,0,0,.4)}
.hero-title .dot{margin:0 14px;font-size:26px;vertical-align:middle}
.hero-btn{margin-top:22px;background:var(--red);color:#fff;font-size:11px;font-weight:700;text-transform:uppercase;padding:9px 22px;border-radius:3px}

/* layout */
.content{display:flex;gap:40px;padding:60px 100px 0}
.main-col{width:660px}
.side-col{width:300px}
.section-title{color:var(--red);font-size:20px;font-weight:700;text-transform:uppercase;margin-bottom:14px;line-height:26px}

/* lot cards */
.lot-card{height:320px;border:1px solid var(--line);margin-bottom:20px;background:#fff}
.lot-title{height:44px;line-height:44px;background:var(--panel);border-bottom:1px solid var(--line);padding:0 18px;font-size:13px;font-weight:700;text-transform:uppercase;color:#444}
.lot-body{display:flex;gap:22px;padding:20px 18px}
.lot-photo{width:260px;height:230px;flex:none;background:linear-gradient(180deg,#a9c2da 0%,#cdd9e2 40%,#8fa36b 70%,#6c7f48 100%)}
.lot-photo.warehouse{background:linear-gradient(180deg,#d8cbb3 0%,#b9a98b 55%,#8b7b60 100%)}
.lot-photo.field{background:linear-gradient(180deg,#b7cfe6 0%,#dbe6ee 45%,#7ea04a 60%,#5f7f33 100%)}
.lot-photo.stone{background:linear-gradient(180deg,#c3d3e0 0%,#d7d2c6 45%,#9a9282 70%,#6f7d4b 100%)}
.lot-info{font-size:12px;color:var(--muted);line-height:1.65}
.lot-info .status{color:var(--red);font-weight:700;font-size:15px;text-transform:uppercase;margin:16px 0 6px}
.lot-info strong{color:var(--ink)}
.lot-actions{display:flex;gap:10px;margin-top:22px}
.btn{display:inline-flex;align-items:center;gap:6px;background:var(--red);color:#fff;font-size:11px;font-weight:700;text-transform:uppercase;padding:8px 18px;border-radius:3px}
.btn svg{width:12px;height:12px;fill:#fff}
.more-row{display:flex;justify-content:flex-end;margin-bottom:50px}

/* sidebar widgets */
.widget{margin-bottom:20px}
.widget-head{background:var(--widget-head);color:#fff;font-size:12px;font-weight:700;text-transform:uppercase;padding:10px 14px;letter-spacing:.5px}
.widget-body{padding:14px 4px 0;font-size:12px;color:var(--muted)}
.field-input{height:32px;border:1px solid var(--line);margin-top:10px;padding:0 10px;line-height:30px;font-size:11px;color:#aaa}
.btn-wide{display:block;text-align:center;margin-top:12px}
.social-row{display:flex;gap:20px;align-items:center;margin-top:12px;font-size:15px;font-weight:700;color:var(--ink)}
.news-item{display:flex;gap:12px;margin-bottom:14px}
.news-thumb{width:90px;height:66px;flex:none;background:linear-gradient(180deg,#c9a48a,#8d6a55)}
.news-thumb.b{background:linear-gradient(180deg,#b9c9d6,#6f8597)}
.news-thumb.c{background:linear-gradient(180deg,#d1b8a0,#96765c)}
.news-title{color:var(--red);font-weight:700;font-size:11px;text-transform:uppercase;line-height:1.4}
.news-date{font-size:11px;color:#999;margin-top:4px}
.centered{text-align:center}
.blog-photo{height:150px;background:linear-gradient(180deg,#c7d6e2 0%,#9fb0a0 55%,#5e7143 100%);margin-bottom:12px}
.avatar{width:120px;height:120px;border-radius:50%;margin:6px auto 12px;background:linear-gradient(180deg,#9a8474,#5b4a40)}
.person{color:var(--red);font-weight:700;font-size:12px;text-transform:uppercase}
.role{font-size:11px;color:#999;margin-bottom:10px}
.about-photo{height:130px;background:linear-gradient(180deg,#b8c8d4,#7c8e6b);margin-bottom:12px}

/* footer */
.site-footer{position:absolute;left:0;top:2730px;width:1200px;height:320px;background:var(--footer);padding:40px 100px 0;display:flex;gap:60px}
.footer-brand{width:260px}
.footer-brand .brand{font-size:20px}
.footer-brand .company{font-weight:700;font-size:12px;margin:10px 0 14px;color:var(--ink)}
.contact-line{display:flex;align-items:center;gap:8px;font-size:12px;color:#555;margin-bottom:8px}
.contact-line svg{width:13px;height:13px;fill:var(--red);flex:none}
.footer-col{width:150px}
.footer-col h4{color:var(--red);font-size:13px;font-weight:700;text-transform:uppercase;margin-bottom:10px}
.footer-col ul{list-style:none;font-size:12px;color:#555;line-height:1.9}
.assoc{width:240px}
.assoc h4{color:var(--red);font-size:13px;font-weight:700;text-transform:uppercase;margin-bottom:14px}
.badges{display:flex;gap:16px;align-items:center}
.badge{width:58px;height:58px;background:#b8b8b8}
.badge.round{border-radius:50%}
.footer-base{position:absolute;left:0;top:3050px;width:1200px;height:50px;background:var(--footer-base);display:flex;align-items:center;justify-content:center;font-size:11px;color:#777}
</style>
</head>
<body>

<header class="site-header">
  <a class="brand" href="#"><span class="brand-mark"></span>brennickauctions.example</a>
  <nav class="main-nav">
    <a class="active" href="#">Home</a>
    <a href="#">Auctions</a>
    <a href="#">Real Estate Listings</a>
    <a href="#">Services</a>
    <a href="#">Appraisals</a>
    <a href="#">The Gavel Hall</a>
    <a href="#">About Us</a>
    <a href="#">Contact Us</a>
  </nav>
</header>

<section class="hero" role="img" aria-label="Large country house with a green lawn and trees under a grey sky">
  <h1 class="hero-title">Personal<span class="dot">•</span>Auctions<span class="dot">•</span>Solutions</h1>
  <a class="hero-btn" href="#">View Our History</a>
</section>

<div class="content">
  <main class="main-col">
    <h2 class="section-title">Featured Listings</h2>

    <article class="lot-card">
      <h3 class="lot-title">Unique Steelcraft Home with Detached Studio</h3>
      <div class="lot-body">
        <div class="lot-photo" role="img" aria-label="Photo of a ranch home with lawn"></div>
        <div class="lot-info">
          <p>Steelcraft home on 1.09 +/- acres with a 24 x 30 detached studio, mature shade trees and a paved drive near town.</p>
          <p class="status">Live On-Site Auction</p>
          <p><strong>Begins:</strong> Thursday, September 30, 2015 at 5:00 PM CDT</p>
          <p><strong>Location:</strong> 3817 Pelham Court, Castor Falls, IN 47088</p>
          <div class="lot-actions">
            <a class="btn" href="#"><svg viewBox="0 0 12 12"><circle cx="5" cy="5" r="3.5" fill="none" stroke="#fff" stroke-width="1.6"/><path d="M7.5 7.5L11 11" stroke="#fff" stroke-width="1.8"/></svg>Details</a>
            <a class="btn" href="#"><svg viewBox="0 0 12 12"><rect x="0" y="3" width="12" height="8" rx="1"/><rect x="4" y="1" width="4" height="3"/></svg>Photos</a>
          </div>
        </div>
      </div>
    </article>

    <article class="lot-card">
      <h3 class="lot-title">Unique Steelcraft Home with Detached Studio</h3>
      <div class="lot-body">
        <div class="lot-photo field" role="img" aria-label="Photo of a farm field with a small building"></div>
        <div class="lot-info">
          <p>Steelcraft home on 1.09 +/- acres with a 24 x 30 detached studio, mature shade trees and a paved drive near town.</p>
          <p class="status">Live On-Site Auction</p>
          <p><strong>Begins:</strong> Thursday, September 30, 2015 at 5:00 PM CDT</p>
          <p><strong>Location:</strong> 3817 Pelham Court, Castor Falls, IN 47088</p>
          <div class="lot-actions">
            <a class="btn" href="#"><svg viewBox="0 0 12 12"><circle cx="5" cy="5" r="3.5" fill="none" stroke="#fff" stroke-width="1.6"/><path d="M7.5 7.5L11 11" stroke="#fff" stroke-width="1.8"/></svg>Details</a>
            <a class="btn" href="#"><svg viewBox="0 0 12 12"><rect x="0" y="3" width="12" height="8" rx="1"/><rect x="4" y="1" width="4" height="3"/></svg>Photos</a>
          </div>
        </div>
      </div>
    </article>

    <article class="lot-card">
      <h3 class="lot-title">Unique Steelcraft Home with Detached Studio</h3>
      <div class="lot-body">
        <div class="lot-photo stone" role="img" aria-label="Photo of a two-storey house with a front yard"></div>
        <div class="lot-info">
          <p>Steelcraft home on 1.09 +/- acres with a 24 x 30 detached studio, mature shade trees and a paved drive near town.</p>
          <p class="status">Live On-Site Auction</p>
          <p><strong>Begins:</strong> Thursday, September 30, 2015 at 5:00 PM CDT</p>
          <p><strong>Location:</strong> 3817 Pelham Court, Castor Falls, IN 47088</p>
          <div class="lot-actions">
            <a class="btn" href="#"><svg viewBox="0 0 12 12"><circle cx="5" cy="5" r="3.5" fill="none" stroke="#fff" stroke-width="1.6"/><path d="M7.5 7.5L11 11" stroke="#fff" stroke-width="1.8"/></svg>Details</a>
            <a class="btn" href="#"><svg viewBox="0 0 12 12"><rect x="0" y="3" width="12" height="8" rx="1"/><rect x="4" y="1" width="4" height="3"/></svg>Photos</a>
          </div>
        </div>
      </div>
    </article>

    <div class="more-row"><a class="btn" href="#">View More Listings</a></div>

    <h2 class="section-title">Featured Auctions</h2>

    <article class="lot-card">
      <h3 class="lot-title">Unique Steelcraft Home with Detached Studio</h3>
      <div class="lot-body">
        <div class="lot-photo warehouse" role="img" aria-label="Photo of stacked goods inside a warehouse"></div>
        <div class="lot-info">
          <p>Steelcraft home on 1.09 +/- acres with a 24 x 30 detached studio, mature shade trees and a paved drive near town.</p>
          <p class="status">Live On-Site Auction</p>
          <p><strong>Begins:</strong> Thursday, September 30, 2015 at 5:00 PM CDT</p>
          <p><strong>Location:</strong> 3817 Pelham Court, Castor Falls, IN 47088</p>
          <div class="lot-actions">
            <a class="btn" href="#"><svg viewBox="0 0 12 12"><circle cx="5" cy="5" r="3.5" fill="none" stroke="#fff" stroke-width="1.6"/><path d="M7.5 7.5L11 11" stroke="#fff" stroke-width="1.8"/></svg>Details</a>
            <a class="btn" href="#"><svg viewBox="0 0 12 12"><rect x="0" y="3" width="12" height="8" rx="1"/><rect x="4" y="1" width="4" height="3"/></svg>Photos</a>
          </div>
        </div>
      </div>
    </article>

    <article class="lot-card">
      <h3 class="lot-title">Unique Steelcraft Home with Detached Studio</h3>
      <div class="lot-body">
        <div class="lot-photo field" role="img" aria-label="Photo of open farmland under a blue sky"></div>
        <div class="lot-info">
          <p>Steelcraft home on 1.09 +/- acres with a 24 x 30 detached studio, mature shade trees and a paved drive near town.</p>
          <p class="status">Live On-Site Auction</p>
          <p><strong>Begins:</strong> Thursday, September 30, 2015 at 5:00 PM CDT</p>
          <p><strong>Location:</strong> 3817 Pelham Court, Castor Falls, IN 47088</p>
          <div class="lot-actions">
            <a class="btn" href="#"><svg viewBox="0 0 12 12"><circle cx="5" cy="5" r="3.5" fill="none" stroke="#fff" stroke-width="1.6"/><path d="M7.5 7.5L11 11" stroke="#fff" stroke-width="1.8"/></svg>Details</a>
            <a class="btn" href="#"><svg viewBox="0 0 12 12"><rect x="0" y="3" width="12" height="8" rx="1"/><rect x="4" y="1" width="4" height="3"/></svg>Photos</a>
          </div>
        </div>
      </div>
    </article>

    <article class="lot-card">
      <h3 class="lot-title">Unique Steelcraft Home with Detached Studio</h3>
      <div class="lot-body">
        <div class="lot-photo" role="img" aria-label="Photo of a small cottage among trees"></div>
        <div class="lot-info">
          <p>Steelcraft home on 1.09 +/- acres with a 24 x 30 detached studio, mature shade trees and a paved drive near town.</p>
          <p class="status">Live On-Site Auction</p>
          <p><strong>Begins:</strong> Thursday, September 30, 2015 at 5:00 PM CDT</p>
          <p><strong>Location:</strong> 3817 Pelham Court, Castor Falls, IN 47088</p>
          <div class="lot-actions">
            <a class="btn" href="#"><svg viewBox="0 0 12 12"><circle cx="5" cy="5" r="3.5" fill="none" stroke="#fff" stroke-width="1.6"/><path d="M7.5 7.5L11 11" stroke="#fff" stroke-width="1.8"/></svg>Details</a>
            <a class="btn" href="#"><svg viewBox="0 0 12 12"><rect x="0" y="3" width="12" height="8" rx="1"/><rect x="4" y="1" width="4" height="3"/></svg>Photos</a>
          </div>
        </div>
      </div>
    </article>

    <div class="more-row"><a class="btn" href="#">View More Auctions</a></div>
  </main>

  <aside class="side-col">
    <section class="widget">
      <h3 class="widget-head">Email Signup</h3>
      <div class="widget-body">
        <p>Get our latest updates through your email!</p>
        <div class="field-input">Enter your name</div>
        <div class="field-input">Enter your email</div>
        <a class="btn btn-wide" href="#">Subscribe Now</a>
      </div>
    </section>

    <section class="widget">
      <h3 class="widget-head">Social Media</h3>
      <div class="widget-body">
        <p>Connect with our social network.</p>
        <div class="social-row"><span>Friendwall</span><span>Chirpline</span><span>ClipStream</span></div>
      </div>
    </section>

    <section class="widget">
      <h3 class="widget-head">News &amp; Events</h3>
      <div class="widget-body">
        <div class="news-item"><div class="news-thumb" role="img" aria-label="News photo of a crowd at an auction"></div><div><p class="news-title">Estate sale draws record crowd to the Gavel Hall</p><p class="news-date">Posted on 21 Sep 2015</p></div></div>
        <div class="news-item"><div class="news-thumb b" role="img" aria-label="News photo of farm equipment"></div><div><p class="news-title">Fall farm machinery auction dates announced</p><p class="news-date">Posted on 18 Sep 2015</p></div></div>
        <div class="news-item"><div class="news-thumb c" role="img" aria-label="News photo of antique furniture"></div><div><p class="news-title">Antique furniture preview open this weekend</p><p class="news-date">Posted on 12 Sep 2015</p></div></div>
        <a class="btn btn-wide" href="#">View More Posts</a>
      </div>
    </section>

    <section class="widget">
      <h3 class="widget-head">Blog</h3>
      <div class="widget-body">
        <div class="blog-photo" role="img" aria-label="Blog photo of a house behind trees"></div>
        <p class="news-title">Five tips to prepare your home for auction day</p>
        <p class="news-date">Posted on 27 Sep 2015</p>
        <p style="margin-top:6px">A well prepared property brings more bidders. Here is how to get ready in a few weeks.</p>
        <a class="btn btn-wide" href="#">View More Posts</a>
      </div>
    </section>

    <section class="widget">
      <h3 class="widget-head">Testimonial</h3>
      <div class="widget-body centered">
        <div class="avatar" role="img" aria-label="Portrait of the client giving the testimonial"></div>
        <p class="person">Marcus Hale</p>
        <p class="role">Satisfied Client</p>
        <p>The team handled our family farm sale with care, clear answers and a great result on auction day.</p>
      </div>
    </section>

    <section class="widget">
      <h3 class="widget-head">About Brennick Auctions</h3>
      <div class="widget-body">
        <div class="about-photo" role="img" aria-label="Photo of the auction office building"></div>
        <p>Family owned since 1978, we serve Indiana sellers with personal auctions, appraisals and real estate.</p>
        <a class="btn btn-wide" href="#">View More Info</a>
      </div>
    </section>
  </aside>
</div>

<footer class="site-footer">
  <div class="footer-brand">
    <a class="brand" href="#"><span class="brand-mark"></span>brennickauctions.example</a>
    <p class="company">Gordon Brennick Auction-Realty</p>
    <p class="contact-line"><svg viewBox="0 0 12 12"><path d="M6 0C3.8 0 2 1.8 2 4c0 3 4 8 4 8s4-5 4-8c0-2.2-1.8-4-4-4zm0 5.6A1.6 1.6 0 1 1 6 2.4a1.6 1.6 0 0 1 0 3.2z"/></svg>3817 Pelham Court • Castor Falls, IN 47088</p>
    <p class="contact-line"><svg viewBox="0 0 12 12"><path d="M0 2h12v8H0z" fill="none" stroke="#d6222f" stroke-width="1.2"/><path d="M0 2l6 5 6-5" fill="none" stroke="#d6222f" stroke-width="1.2"/></svg>dominic@brennickauctions.example</p>
    <p class="contact-line"><svg viewBox="0 0 12 12"><path d="M2.5 0.5l2 2.5-1 1.5c.8 1.6 2.4 3.2 4 4l1.5-1 2.5 2-1.5 2C5 11 1 7 0.5 2z"/></svg>812.555.0146</p>
    <p class="contact-line"><svg viewBox="0 0 12 12"><path d="M2.5 0.5l2 2.5-1 1.5c.8 1.6 2.4 3.2 4 4l1.5-1 2.5 2-1.5 2C5 11 1 7 0.5 2z"/></svg>877.555.0193</p>
  </div>
  <div class="footer-col">
    <h4>Brennick</h4>
    <ul><li>Home</li><li>Auctions</li><li>Real Estate Listings</li><li>Services</li><li>Appraisals</li><li>The Gavel Hall</li><li>About Us</li></ul>
  </div>
  <div class="footer-col">
    <h4>Information</h4>
    <ul><li>Terms &amp; Conditions</li><li>Privacy Policy</li><li>Disclaimer</li><li>Sitemap</li></ul>
  </div>
  <div class="assoc">
    <h4>Associations</h4>
    <div class="badges">
      <div class="badge" role="img" aria-label="Association membership badge"></div>
      <div class="badge round" role="img" aria-label="Association membership badge"></div>
      <div class="badge" role="img" aria-label="Association membership badge"></div>
    </div>
  </div>
</footer>
<div class="footer-base">Copyright © 2015 - Brennick Auction Realty Inc. - All Rights Reserved</div>

</body>
</html>
```